Creative Web Designer: Refresh & Elevate our Beach Lifestyle Brand with a Joyful, Elegant Red...

Corallune (corallune.gr), a vibrant Greek brand celebrated for its high-quality beachwear and accessories, is embarking on an exciting phase as we enter our third year. Renowned for our stylish flip flops, beach towels, and caps, we are thrilled to announce the expansion of our product line with innovative beach essentials and a fresh palette for our existing collection.
As we continue to grow and evolve, we are in search of a talented and imaginative web designer who can capture the essence of Corallune and translate it into a digital experience. Our ideal candidate will craft a website that mirrors the happiness and relaxation of a day at the beach, while also embodying the sophistication and elegance that our brand represents.
Your Mission:
Design a Website That Reflects Our Brand Identity: Create a website that is visually stunning, easy to navigate, and showcases our products in a way that feels both refreshing and luxurious.
Incorporate New Product Lines and Colors: Seamlessly integrate our new beach products and color schemes, ensuring the website remains cohesive and on-brand.
User Experience is Key: Design a user-friendly interface that ensures a seamless shopping experience for our customers, with intuitive navigation and a mobile-responsive design.
Embrace Creativity While Staying Elegant: We want our website to be a reflection of the joy and elegance that our products bring to our customers. Your design should be innovative, incorporating modern web design trends that align with our brand's aesthetic.
What We're Looking For:
A portfolio that demonstrates experience in creating visually appealing and user-friendly e-commerce websites.
Strong understanding of branding and the ability to translate a brand's essence into a digital format.
Proficiency in the latest web design software and technologies.
Excellent communication skills and the ability to work collaboratively with our team to bring our vision to life.
This is a fantastic opportunity for a web designer who loves the beach lifestyle and is passionate about creating beautiful, effective websites. If you're ready to dive into a project that will challenge and excite you, while making a significant impact on our growing brand, we would love to hear from you.
Regarding the products, on the website (corallune.gr) you will the flips flops and on the attached powerpoint all the accessories for this summer. Please use the images to craft your designs.
Join us in making Corallune the go-to brand for beach enthusiasts everywhere. Apply now to start the conversation and share your vision for our new website 😊🩴☀️⛱️
p.s. we didn;t mention the pages to be designed. Its 4 pages in all,
homepage, product category page, singleproduct page and contact us page

```html
<!DOCTYPE html>
<html lang="en">
<head>
<meta charset="utf-8">
<title>Corallune — Summerwear</title>
<link rel="stylesheet" href="https://fonts.googleapis.com/css2?family=Krona+One&family=Jost:ital,wght@0,400;0,500;0,600;1,400&display=swap">
<style>
:root{
  --navy:#16135e;
  --ink:#0f0c2c;
  --dark:#0c0b16;
  --mint:#cfe3cc;
  --mint-soft:#eef6ef;
  --card:#f2f7f2;
  --green:#3fc43a;
  --gold:#f5b50a;
  --grey:#6b6b74;
  --white:#ffffff;
}
*{margin:0;padding:0;box-sizing:border-box}
html,body{width:1200px;height:5042px;overflow:hidden}
body{position:relative;background:var(--white);font-family:"Jost",sans-serif;color:var(--ink)}
.abs{position:absolute}
.fill{position:absolute}
.heading{font-family:"Krona One",sans-serif;color:var(--navy);text-transform:uppercase;letter-spacing:.5px;font-weight:400}
svg{display:block}

/* promo bar */
.promo-bar{left:0;top:0;width:1200px;height:43px;background:var(--ink);color:#fff;font-size:13px}
.promo-bar .msg{position:absolute;left:0;width:1200px;text-align:center;top:12px}
.promo-bar .lang{position:absolute;right:56px;top:12px;display:flex;gap:6px;align-items:center}

/* nav */
.site-nav{left:0;top:43px;width:1200px;height:90px}
.brand{position:absolute;left:86px;top:24px;font-size:28px;font-weight:600;color:var(--navy)}
.menu{position:absolute;top:34px;left:245px;display:flex;gap:34px;font-size:14px;font-weight:500}
.search{position:absolute;left:726px;top:27px;width:196px;height:38px;background:#f0f0f2;border-radius:2px;font-size:12px;color:#9a9aa2;padding:11px 12px}
.search svg{position:absolute;right:12px;top:10px}
.account{position:absolute;left:949px;top:34px;font-size:14px;display:flex;gap:6px;align-items:center}
.cart{position:absolute;left:1049px;top:34px;font-size:14px;display:flex;gap:6px;align-items:center}
.cart .count{position:absolute;left:15px;top:-8px;width:14px;height:14px;border-radius:50%;background:var(--navy);color:#fff;font-size:9px;text-align:center;line-height:14px}

/* hero */
.hero-panel{left:0;top:133px;width:317px;height:525px;background:var(--mint)}
.hero-scene{left:317px;top:133px;width:883px;height:525px;background:linear-gradient(180deg,#a9cde6 0%,#c6ddec 38%,#3f86b6 52%,#9fc3d6 60%,#e8dcc4 72%,#d9c29c 100%)}
.hero-model{left:699px;top:153px;width:395px;height:571px;background:linear-gradient(180deg,#7faed4 0%,#a8c7dd 30%,#5f9a5a 42%,#6fa7c4 50%,#e6dac3 62%,#d2b994 100%)}
.hero-title{left:86px;top:277px;font-size:36px;line-height:53px;color:var(--ink)}
.hero-sub{left:87px;top:393px;font-size:15px}
.btn-outline{left:85px;top:444px;width:185px;height:41px;border:1.5px solid var(--navy);font-size:12px;letter-spacing:2px;font-weight:500;display:flex;align-items:center;justify-content:center;gap:8px;color:var(--navy)}
.slide-count{left:86px;top:572px;font-size:34px}
.slide-count small{font-size:13px}
.scroll-line{left:599px;top:607px;width:1px;height:98px;background:var(--ink)}
.scroll-line.b{left:606px;top:598px;height:92px}
.scroll-label{left:557px;top:709px;font-size:14px}

/* section titles */
.sec-title{left:0;width:1200px;text-align:center;font-size:28px}
.sec-sub{left:0;width:1200px;text-align:center;font-size:14px}

/* arrivals */
.arrival{top:887px;width:246px;height:307px;background:var(--card)}
.arrival .pic{position:absolute;left:18px;top:20px;width:210px;height:190px}
.arrival .name{position:absolute;top:222px;width:100%;text-align:center;font-family:"Krona One",sans-serif;font-size:14px;color:var(--navy)}
.arrival .price{position:absolute;top:249px;width:100%;text-align:center;font-size:13px;color:var(--grey)}
.arrival .cta{position:absolute;top:274px;width:100%;text-align:center;font-size:12px;letter-spacing:2px;color:var(--navy);font-weight:500}
.arrival .cta span{border-bottom:1.5px solid var(--navy);padding-bottom:2px}
.btn-dark{width:166px;height:43px;background:var(--dark);color:#fff;font-size:12px;letter-spacing:2px;font-weight:500;display:flex;align-items:center;justify-content:center;gap:8px}

/* feature */
.feature-band{left:0;top:1315px;width:1200px;height:658px;background:var(--mint-soft)}
.feature-title{left:84px;top:1382px;font-size:28px}
.feature-sub{left:86px;top:1417px;font-size:14px}
.arrow-box{width:44px;height:40px;border:1.5px solid var(--ink);display:flex;align-items:center;justify-content:center}
.feature-pic{top:1452px;width:328px;height:405px}
.item-name{font-family:"Krona One",sans-serif;font-size:15px;color:var(--navy)}
.item-price{font-size:13px;color:var(--grey)}

/* rubber banner */
.rubber-band{left:0;top:1973px;width:1200px;height:655px;background:linear-gradient(180deg,#ebdbd4 0%,#e8d3ca 58%,#f6f3f1 72%,#e2cfc3 82%,#cfae97 100%)}
.rubber-pic{left:611px;top:2022px;width:502px;height:606px;background:linear-gradient(165deg,#f1ecd8 0%,#dcd6bf 28%,#a79e90 45%,#f2b8c8 60%,#2f6e55 72%,#8a8070 100%)}
.rubber-t1{left:157px;top:2196px;font-size:29px}
.rubber-t2{left:157px;top:2236px;font-size:29px}
.rubber-t2 .green{color:var(--green)}
.rubber-t3{left:157px;top:2290px;font-size:22px;color:#4a4a55;letter-spacing:1px}

/* top selling */
.seller-pic{top:2799px;width:330px;height:225px;background:var(--card)}
.seller-pic .obj{position:absolute;left:65px;top:12px;width:200px;height:200px}

/* reviews */
.review-band{left:0;top:3288px;width:1200px;height:659px;background:var(--mint-soft)}
.review-intro{left:250px;width:700px;top:3386px;text-align:center;font-size:15px;line-height:29px;padding:0 40px}
.review{top:3465px;width:320px;text-align:center}
.review .avatar{position:relative;margin:0 auto;width:104px;height:104px;border-radius:50%;border:4px solid #fff;background:linear-gradient(180deg,#e6e9ee 0%,#c9ced6 55%,#3a3f55 100%)}
.review .quote{position:absolute;right:-20px;bottom:-8px;font-family:"Krona One",sans-serif;font-size:42px;color:var(--gold);line-height:30px}
.review .text{margin-top:20px;font-style:italic;font-size:14.5px;line-height:27px;color:#555560}
.review .stars{margin-top:10px;display:flex;justify-content:center}
.review .who{margin-top:12px;font-size:17px;font-weight:500;color:var(--navy)}
.review .role{font-style:italic;font-size:14px;color:var(--grey);margin-top:4px}

/* gallery */
.gallery-tile{top:3947px;width:300px;height:294px}

/* newsletter */
.news-title{left:86px;top:4356px;font-size:30px}
.news-text{left:86px;top:4400px;font-size:17px;line-height:30px}
.news-text b{font-weight:600}
.news-input{left:415px;top:4412px;width:495px;height:38px;border-bottom:1.5px solid #8a8a94;font-size:15px;color:#9a9aa2}

/* footer */
.footer{left:0;top:4575px;width:1200px;height:467px;background:radial-gradient(ellipse at 50% 0%,#1a1a2a 0%,#0c0b14 70%)}
.foot-head{top:4691px;font-family:"Krona One",sans-serif;font-size:11px;letter-spacing:2.5px;color:#fff}
.foot-list{top:4730px;font-size:14px;line-height:38px;color:#e6e6ec;list-style:none}
.contact-row{display:flex;gap:14px;align-items:flex-start;font-size:14px;color:#e6e6ec;line-height:24px}
.social{left:969px;top:4740px;display:flex;gap:26px}
.social span{width:16px;height:16px;border-radius:50%;background:#fff;display:block}
.foot-copy{left:86px;top:5003px;font-size:13px;color:#7d7d88}
.foot-copy b{color:#fff;font-weight:600}
.foot-date{left:926px;top:5003px;font-size:13px;color:#7d7d88}
.pay{top:4962px;left:802px;display:flex;gap:7px}
.pay span{width:39px;height:25px;border-radius:4px;display:block}
</style>
</head>
<body>

<div class="abs promo-bar">
  <div class="msg">Get 20% off on our selected items</div>
  <div class="lang">ENG <svg width="10" height="6" viewBox="0 0 10 6"><path d="M1 1l4 4 4-4" stroke="#fff" fill="none" stroke-width="1.5"/></svg></div>
</div>

<header class="abs site-nav">
  <div class="brand">Corallune</div>
  <nav class="menu"><span>Home</span><span>Product Category</span><span>Single Product</span><span>Contact Us</span></nav>
  <div class="search">Search
    <svg width="17" height="17" viewBox="0 0 17 17"><circle cx="7" cy="7" r="5.5" stroke="#6b6b74" stroke-width="1.5" fill="none"/><path d="M11 11l5 5" stroke="#6b6b74" stroke-width="1.5"/></svg>
  </div>
  <div class="account"><svg width="16" height="17" viewBox="0 0 16 17"><circle cx="8" cy="5" r="4" stroke="#0f0c2c" stroke-width="1.4" fill="none"/><path d="M1 16c0-4 3-6 7-6s7 2 7 6" stroke="#0f0c2c" stroke-width="1.4" fill="none"/></svg>Account</div>
  <div class="cart"><svg width="20" height="18" viewBox="0 0 20 18"><path d="M1 1h3l2.5 11h10l2-8H5" stroke="#0f0c2c" stroke-width="1.4" fill="none"/><circle cx="8" cy="15.5" r="1.5" fill="#0f0c2c"/><circle cx="15" cy="15.5" r="1.5" fill="#0f0c2c"/></svg><span class="count">0</span>Cart</div>
</header>

<!-- hero -->
<div class="fill hero-panel"></div>
<div class="fill hero-scene" role="img" aria-label="Beach with palm leaves, blue sea and sand, a patterned scrunchie on the shore"></div>
<div class="fill hero-model" role="img" aria-label="Model on a palm-lined beach wearing a black top and a patterned beach sarong"></div>
<h1 class="abs heading hero-title">New Summer<br>Collection</h1>
<p class="abs hero-sub">Explore Our high-quality beachwear and accessories</p>
<div class="abs btn-outline">SHOP NOW <svg width="26" height="8" viewBox="0 0 26 8"><path d="M0 4h24M20 1l4 3-4 3" stroke="#16135e" stroke-width="1.3" fill="none"/></svg></div>
<div class="abs slide-count">1<span style="font-size:30px">/</span><small>4</small></div>
<div class="abs scroll-line"></div>
<div class="abs scroll-line b"></div>
<div class="abs scroll-label">Scrolldown</div>

<!-- new arrivals -->
<h2 class="abs heading sec-title" style="top:798px">New Arrivals</h2>
<p class="abs sec-sub" style="top:834px">Check what's new</p>

<div class="abs arrival" style="left:84px">
  <div class="pic" role="img" aria-label="Printed beach pouch with a crab motif" style="background:radial-gradient(ellipse 48% 36% at 52% 50%,#f2a886 0%,#f4c9a4 45%,#f3e6d6 75%,rgba(242,247,242,0) 100%)"></div>
  <div class="name">POUCHES</div><div class="price">€ 45.00</div>
</div>
<div class="abs arrival" style="left:346px">
  <div class="pic" role="img" aria-label="White canvas tote bag with an abstract print" style="background:radial-gradient(ellipse 28% 44% at 50% 55%,#c99a52 0%,#e9e5de 45%,#f7f6f3 72%,rgba(242,247,242,0) 100%)"></div>
  <div class="name">TOTE BAGS</div><div class="price">€ 45.00</div>
</div>
<div class="abs arrival" style="left:607px">
  <div class="pic" role="img" aria-label="Folded umbrella with a colourful abstract print" style="background:radial-gradient(ellipse 48% 32% at 50% 48%,#e78e66 0%,#f1c08f 35%,#a8cfa6 60%,#f2e6cc 78%,rgba(242,247,242,0) 100%)"></div>
  <div class="name">UMBRELLA</div><div class="price">€ 45.00</div>
  <div class="cta"><span>ADD TO CART</span></div>
</div>
<div class="abs arrival" style="left:869px">
  <div class="pic" role="img" aria-label="Bucket hat with a colourful abstract print" style="background:radial-gradient(ellipse 46% 26% at 50% 54%,#e8a080 0%,#b8d4b6 40%,#efd7b6 65%,rgba(242,247,242,0) 100%)"></div>
  <div class="name">BUCKETS</div><div class="price">€ 45.00</div>
</div>
<svg class="abs" style="left:822px;top:1183px" width="26" height="28" viewBox="0 0 26 28"><path d="M8 2v14l-3-3-3 2 6 10h12l3-9-1-6-4-1-1 2-1-3-3 0-1 2V2z" fill="#fff" stroke="#0f0c2c" stroke-width="1.3"/></svg>
<div class="abs btn-dark" style="left:517px;top:1225px">VIEW ALL <svg width="26" height="8" viewBox="0 0 26 8"><path d="M0 4h24M20 1l4 3-4 3" stroke="#fff" stroke-width="1.3" fill="none"/></svg></div>

<!-- feature product -->
<div class="fill feature-band"></div>
<h2 class="abs heading feature-title">Feature Product</h2>
<p class="abs feature-sub">Check what's new</p>
<div class="abs arrow-box" style="left:1008px;top:1389px"><svg width="26" height="14" viewBox="0 0 26 14"><path d="M25 7H2M7 2L2 7l5 5M2 1v12" stroke="#0f0c2c" stroke-width="1.4" fill="none"/></svg></div>
<div class="abs arrow-box" style="left:1071px;top:1389px"><svg width="26" height="14" viewBox="0 0 26 14"><path d="M1 7h23M19 2l5 5-5 5M24 1v12" stroke="#0f0c2c" stroke-width="1.4" fill="none"/></svg></div>

<div class="fill feature-pic" style="left:86px;background:linear-gradient(180deg,#d7dade 0%,#a9a39b 22%,#c45a33 45%,#d97a48 62%,#ef7a2a 80%,#8aa6b4 92%,#55707c 100%)" role="img" aria-label="Woman in a smocked summer dress under a striped parasol holding orange flip flops"></div>
<div class="fill feature-pic" style="left:436px;background:linear-gradient(180deg,#1fb2c6 0%,#49cdd0 40%,#8fdcd8 52%,#f5f3ee 66%,#ef8a5a 82%,#eadfca 100%)" role="img" aria-label="Woman sitting on white sand beside a striped beach bag facing a turquoise sea"></div>
<div class="fill feature-pic" style="left:785px;background:linear-gradient(180deg,#e9ddc8 0%,#9fbf8c 28%,#e6b68a 40%,#eeeee8 58%,#dcdcd6 78%,#5f8250 100%)" role="img" aria-label="Woman in a green cap and white dress holding a colourful printed umbrella"></div>

<div class="abs item-name" style="left:86px;top:1876px">SUNSET</div><div class="abs item-price" style="left:86px;top:1898px">€ 19.90</div>
<div class="abs item-name" style="left:436px;top:1876px">BEACH BAGS</div><div class="abs item-price" style="left:436px;top:1898px">€ 28.90</div>
<div class="abs item-name" style="left:785px;top:1876px">UMBRELLA</div><div class="abs item-price" style="left:785px;top:1898px">€ 19.90</div>

<!-- flip flops banner -->
<div class="fill rubber-band" role="img" aria-label="Sandy shore with sea foam"></div>
<div class="fill rubber-pic" role="img" aria-label="Legs in pink flip flops on a wooden boardwalk beside a straw hat"></div>
<div class="abs heading rubber-t1">From 100%</div>
<div class="abs heading rubber-t2"><span class="green">Natural</span> Rubber</div>
<div class="abs rubber-t3">FLIP FLOPS</div>
<div class="abs btn-dark" style="left:157px;top:2341px;width:183px;height:41px">SHOP NOW <svg width="26" height="8" viewBox="0 0 26 8"><path d="M0 4h24M20 1l4 3-4 3" stroke="#fff" stroke-width="1.3" fill="none"/></svg></div>

<!-- top selling -->
<h2 class="abs heading sec-title" style="top:2734px">Top Selling Product</h2>
<div class="abs seller-pic" style="left:86px"><div class="obj" role="img" aria-label="Backpack beach bag with a colourful abstract print" style="background:radial-gradient(ellipse 24% 45% at 50% 50%,#e98f6a 0%,#f3c8a8 35%,#9ccaa6 60%,#f3e6d8 80%,rgba(242,247,242,0) 100%)"></div></div>
<div class="abs seller-pic" style="left:434px"><div class="obj" role="img" aria-label="Printed jockey cap with a green brim" style="background:radial-gradient(ellipse 40% 24% at 50% 55%,#e6a47c 0%,#f0cba2 35%,#5f9460 62%,#e6eee2 82%,rgba(242,247,242,0) 100%)"></div></div>
<div class="abs seller-pic" style="left:781px"><div class="obj" role="img" aria-label="Tote beach bag with a colourful abstract print" style="background:radial-gradient(ellipse 38% 40% at 50% 58%,#4f8fc9 0%,#e9876a 32%,#f2cf7a 55%,#f4ebde 78%,rgba(242,247,242,0) 100%)"></div></div>
<svg class="abs" style="left:65px;top:2895px" width="46" height="38" viewBox="0 0 46 38"><path d="M45 19H6M13 12l-7 7 7 7M6 4v30h30V30M36 8V4H6" stroke="#0f0c2c" stroke-width="1.4" fill="none"/></svg>
<svg class="abs" style="left:1090px;top:2895px" width="46" height="38" viewBox="0 0 46 38"><path d="M1 19h39M33 12l7 7-7 7M40 4v30H10V30M10 8V4h30" stroke="#0f0c2c" stroke-width="1.4" fill="none"/></svg>

<div class="abs item-name" style="left:86px;top:3043px">BEACH BAG</div><div class="abs item-price" style="left:86px;top:3074px">€ 35.00</div>
<div class="abs item-name" style="left:434px;top:3043px">JOCKEY CAPS</div><div class="abs item-price" style="left:434px;top:3074px">€ 35.00</div>
<div class="abs item-name" style="left:782px;top:3043px">BEACH BAGS</div><div class="abs item-price" style="left:782px;top:3074px">€ 35.00</div>
<div class="abs btn-dark" style="left:517px;top:3129px;height:41px">VIEW ALL <svg width="26" height="8" viewBox="0 0 26 8"><path d="M0 4h24M20 1l4 3-4 3" stroke="#fff" stroke-width="1.3" fill="none"/></svg></div>

<!-- client review -->
<div class="fill review-band"></div>
<h2 class="abs heading sec-title" style="top:3349px">Client Review</h2>
<p class="abs review-intro">Lorem ipsum dolor sit amet, consectetur adipiscing elit. Ut feugiat eleifend ipsum, eu facilisis nunc sodales</p>

<svg width="0" height="0" style="position:absolute"><defs><path id="st" d="M7.5 0l2.2 4.8 5.3.6-3.9 3.6 1.1 5.2-4.7-2.7-4.7 2.7 1.1-5.2L0 5.4l5.3-.6z"/></defs></svg>

<div class="abs review" style="left:81px">
  <div class="avatar" role="img" aria-label="Customer portrait"><span class="quote">“</span></div>
  <p class="text">Maecenas id massa metus. Aliquam vitae quam justo. Cras eget maorem. Vestibulum maximus tellus quu mattis sodales. Integer sit amet nisi ac risus tincidunt tincidunt et eu ante.</p>
  <div class="stars"><svg width="80" height="15" viewBox="0 0 80 15"><g fill="#f5b50a"><use href="#st"/><use href="#st" x="16"/><use href="#st" x="32"/><use href="#st" x="48"/><use href="#st" x="64"/></g></svg></div>
  <div class="who">Leo Marsh</div><div class="role">Customer</div>
</div>
<div class="abs review" style="left:439px">
  <div class="avatar" role="img" aria-label="Customer portrait" style="background:linear-gradient(180deg,#ece4e4 0%,#cfc2c4 55%,#4a4f6a 100%)"><span class="quote">“</span></div>
  <p class="text">Maecenas id massa metus. Aliquam vitae quam justo. Cras eget maorem. Vestibulum maximus tellus quu mattis sodales. Integer sit amet nisi ac risus tincidunt tincidunt et eu ante.</p>
  <div class="stars"><svg width="80" height="15" viewBox="0 0 80 15"><g fill="#f5b50a"><use href="#st"/><use href="#st" x="16"/><use href="#st" x="32"/><use href="#st" x="48"/><use href="#st" x="64"/></g></svg></div>
  <div class="who">Nora Vale</div><div class="role">Customer</div>
</div>
<div class="abs review" style="left:795px">
  <div class="avatar" role="img" aria-label="Customer portrait" style="background:linear-gradient(180deg,#ebebeb 0%,#cbc6c3 55%,#8a8582 100%)"><span class="quote">“</span></div>
  <p class="text">Maecenas id massa metus. Aliquam vitae quam justo. Cras eget maorem. Vestibulum maximus tellus quu mattis sodales. Integer sit amet nisi ac risus tincidunt tincidunt et eu ante.</p>
  <div class="stars"><svg width="80" height="15" viewBox="0 0 80 15"><g fill="#f5b50a"><use href="#st"/><use href="#st" x="16"/><use href="#st" x="32"/><use href="#st" x="48"/><use href="#st" x="64"/></g></svg></div>
  <div class="who">Theo Grant</div><div class="role">Customer</div>
</div>
<svg class="abs" style="left:561px;top:3870px" width="80" height="14" viewBox="0 0 80 14"><path d="M31 7H2M7 2L2 7l5 5M49 7h29M73 2l5 5-5 5" stroke="#0f0c2c" stroke-width="1.5" fill="none"/></svg>

<!-- gallery -->
<div class="fill gallery-tile" style="left:0;background:linear-gradient(120deg,#b97a3a 0%,#e0b277 30%,#f4f1ea 55%,#3f8ab0 85%,#9a6a38 100%)" role="img" aria-label="Smiling woman in a white sun hat on a rocky coast"></div>
<div class="fill gallery-tile" style="left:300px;background:linear-gradient(180deg,#7aa6c0 0%,#2f6f92 40%,#e8e4dc 62%,#2d6688 80%,#b08a5a 100%)" role="img" aria-label="Woman with a straw bag walking into the sea"></div>
<div class="fill gallery-tile" style="left:600px;background:linear-gradient(180deg,#b6d0e0 0%,#f1ece0 30%,#e7c6a4 50%,#d23a2e 72%,#e9e1d4 100%)" role="img" aria-label="Woman in a wide white hat and red top by the sea"></div>
<div class="fill gallery-tile" style="left:900px;background:linear-gradient(135deg,#1f5fa8 0%,#f1ede4 30%,#3f7fc2 45%,#d8c69f 65%,#5b93cf 100%)" role="img" aria-label="Striped towel, straw hat and blue flip flops on wooden planks"></div>

<!-- newsletter -->
<h2 class="abs heading news-title">Newsletter</h2>
<p class="abs news-text">Subscribe to our Newsletter and<br>Receive<b>15% Off</b> your next order</p>
<div class="abs news-input">Enter Emai address</div>
<div class="abs btn-dark" style="left:959px;top:4409px;width:155px;height:41px">SUBSCRIBE <svg width="26" height="8" viewBox="0 0 26 8"><path d="M0 4h24M20 1l4 3-4 3" stroke="#fff" stroke-width="1.3" fill="none"/></svg></div>

<!-- footer -->
<footer class="fill footer"></footer>
<div class="abs foot-head" style="left:84px">CONTACT INFO</div>
<div class="abs foot-head" style="left:448px">USEFUL LINKS</div>
<div class="abs foot-head" style="left:714px">OTHER LINKS</div>
<div class="abs foot-head" style="left:969px">FOLLOW US</div>

<div class="abs" style="left:84px;top:4733px;display:flex;flex-direction:column;gap:12px">
  <div class="contact-row"><svg width="16" height="16" viewBox="0 0 16 16" style="margin-top:4px"><path d="M8 1l7 7-7 7-7-7z" fill="#f5b50a"/><circle cx="8" cy="8" r="2" fill="#0c0b16"/></svg><span>Corallune IKE, Thalassis 12,<br>Nea Smyrni, 171 21, Athens</span></div>
  <div class="contact-row"><svg width="16" height="16" viewBox="0 0 16 16" style="margin-top:4px"><path d="M3 1l3 3-2 2c1 2.5 3.5 5 6 6l2-2 3 3-2 2C7 15 1 9 1 3z" fill="#f5b50a"/></svg><span>+30 210 555 0142</span></div>
  <div class="contact-row"><svg width="16" height="16" viewBox="0 0 16 16" style="margin-top:4px"><path d="M3 1l3 3-2 2c1 2.5 3.5 5 6 6l2-2 3 3-2 2C7 15 1 9 1 3z" fill="#f5b50a"/></svg><span>+30 690 555 0178</span></div>
  <div class="contact-row"><svg width="16" height="16" viewBox="0 0 16 16" style="margin-top:4px"><rect x="1" y="3" width="14" height="10" rx="1" fill="#f5b50a"/><path d="M1 4l7 5 7-5" stroke="#0c0b16" stroke-width="1.2" fill="none"/></svg><span>info@corallune.gr</span></div>
</div>

<ul class="abs foot-list" style="left:448px"><li>Terms of use</li><li>Privacy Policy</li><li>Payment Methods</li><li>Return Policy</li></ul>
<ul class="abs foot-list" style="left:714px"><li>Missions</li><li>Contact</li><li>About us</li><li>Download our catalogue</li></ul>

<div class="abs social"><span></span><span></span><span></span><span></span></div>

<div class="abs pay">
  <span style="background:#e8e8ee"></span>
  <span style="background:#f2a33a"></span>
  <span style="background:#3b5bb8"></span>
  <span style="background:#d8d8de"></span>
  <span style="background:#4f8fd8"></span>
  <span style="background:#2a56a8"></span>
  <span style="background:#cfe0f0"></span>
</div>
<div class="abs foot-copy">© 2024 <b>Corallune</b> All right reserved</div>
<div class="abs foot-date">February 22, 2024.</div>

</body>
</html>
```